Redwell - Rebranding, Namecard, Stationary and One Page Web

Refresh logo, make it modern and design matching name card, stationary and one page web

Redwell Information Technology (Int'l) Company Limited
紅井訊息科技(國際)有限公司

Company is System Integrator, and will be providing products and services to government and enterprise organizations. Our Chief Security Officer came from top U.S. vendor, and had been working on top enterprise and government projects globally, so we want the refreshed image of the new company to have a East Cost U.S. style, with hint of technology from Silicon Valley. The company will also be representing top brands from the U.S. on information security.

Branding refresh is needed because company is being acquired and is expanding

Target Market(s)

Cyber Security

Industry/Entity Type

Information Technology

Contact Information for Business Card

Need Chinese and English

Number of Pages Required

1 page

Font styles to use
Sans Serif

Colors
0292cd
00a990

Requirements
Must have
• Modern, clean, cyber look. Must keep same colors and general look and feel of original logo. Only modernization, do not change its personality

```html
<!DOCTYPE html>
<html lang="en">
<head>
<meta charset="utf-8">
<title>Redwell Name Card</title>
<link rel="stylesheet" href="https://fonts.googleapis.com/css2?family=Open+Sans:wght@400;600;700&family=Noto+Sans+TC:wght@400&display=swap">
<style>
  :root {
    --teal: #13ad97;
    --blue: #4a8fc4;
    --sky: #c4e2f3;
    --white: #ffffff;
    --paper: #fbfbfb;
    --bg: #ece9e4;
    --ink-soft: rgba(255,255,255,0.92);
  }
  * { margin: 0; padding: 0; box-sizing: border-box; }
  html, body { width: 1200px; height: 1200px; overflow: hidden; background: var(--bg); }
  body { position: relative; font-family: "Open Sans", sans-serif; }

  .card {
    position: absolute; left: 180px; width: 840px; height: 480px;
    background: var(--paper); box-shadow: 0 6px 22px rgba(0,0,0,0.12); overflow: hidden;
  }
  .card--front { top: 80px; }
  .card--back { top: 640px; }

  .card__bands { position: absolute; inset: 0; }

  .brand {
    position: absolute; display: flex; align-items: center; gap: 14px;
    color: var(--blue); font-weight: 700; letter-spacing: 1px;
  }
  .brand__dot { width: 22px; height: 22px; border-radius: 50%; background: var(--teal); }
  .card--front .brand { left: 52px; top: 48px; font-size: 52px; }
  .card--back .brand { left: 50%; top: 50%; transform: translate(-50%, -50%); font-size: 64px; }

  .holder { position: absolute; left: 580px; top: 200px; color: var(--white); }
  .holder__name { font-size: 30px; font-weight: 700; letter-spacing: 0.5px; }
  .holder__title { font-size: 13px; font-weight: 400; margin-left: 6px; vertical-align: top; }

  .contact { position: absolute; left: 40px; top: 300px; color: var(--ink-soft); font-size: 16px; line-height: 1.55; }
  .contact__company { font-size: 15px; }
  .contact__company-zh { font-family: "Noto Sans TC", sans-serif; font-size: 15px; margin-bottom: 4px; }
  .contact__row { display: flex; align-items: center; gap: 8px; }
  .contact__row svg { width: 14px; height: 14px; flex: none; }

  .divider { position: absolute; left: 548px; top: 300px; width: 1px; height: 140px; background: rgba(255,255,255,0.7); }

  .address { position: absolute; left: 566px; top: 300px; width: 260px; color: var(--ink-soft); font-size: 14px; line-height: 1.55; display: flex; gap: 8px; }
  .address svg { width: 14px; height: 14px; flex: none; margin-top: 3px; }
</style>
</head>
<body>

<section class="card card--front">
  <svg class="card__bands" viewBox="0 0 840 480" aria-hidden="true">
    <polygon points="0,226 500,226 530,170 840,170 840,180 538,180 508,236 0,236" fill="var(--sky)"/>
    <polygon points="0,250 515,250 548,180 840,180 840,480 0,480" fill="var(--teal)"/>
  </svg>

  <div class="brand"><span class="brand__dot"></span>Redwell</div>

  <div class="holder">
    <span class="holder__name">DANIEL WONG</span><span class="holder__title">CEO</span>
  </div>

  <div class="contact">
    <p class="contact__company">Redwell Information Technology (Int'l) Company Limited</p>
    <p class="contact__company-zh">紅井訊息科技(國際)有限公司</p>
    <p class="contact__row">
      <svg viewBox="0 0 16 16"><path d="M4 1l3 3-2 2c1 2 3 4 5 5l2-2 3 3-2 3C7 15 1 9 1 3z" fill="#fff"/></svg>
      (852) 5120 4876
    </p>
    <p class="contact__row">
      <svg viewBox="0 0 16 16"><circle cx="8" cy="8" r="7" fill="none" stroke="#fff" stroke-width="1.5"/><path d="M1 8h14M8 1c-3 4-3 10 0 14M8 1c3 4 3 10 0 14" fill="none" stroke="#fff" stroke-width="1.2"/></svg>
      www.hkredwell.com.hk
    </p>
    <p class="contact__row">
      <svg viewBox="0 0 16 16"><rect x="1" y="3" width="14" height="10" fill="none" stroke="#fff" stroke-width="1.5"/><path d="M1 3l7 6 7-6" fill="none" stroke="#fff" stroke-width="1.5"/></svg>
      danielwong@hkredwell.com.hk
    </p>
  </div>

  <div class="divider"></div>

  <div class="address">
    <svg viewBox="0 0 16 16"><path d="M8 1l7 6h-2v8H3V7H1z" fill="#fff"/></svg>
    <p>Office: Room B, Unit 208, 2/F, Lok Tin Ind. Bldg, No 15 Hing Yip Road, Kwun Tong, Kowloon, HKSAR</p>
  </div>
</section>

<section class="card card--back">
  <div class="brand"><span class="brand__dot"></span>Redwell</div>
</section>

</body>
</html>
```